TEK Logistics - Banner 2.5' x 8' for 20+ locations

Need a banner designed that will pop. This banner will be displayed at over 20 of our transportation facilities. Goal is for the banner to grab the attention of employees, contractors and clients and help reinforce our mission and core values. Designed needs to include TEK Logo, our core values and mission statement. Red and Black are the main company colors and we need to stay within that theme and color pallet. Attached is a previous version that was too basic and boring. Willing to consider a design that excludes the mission statement.

Gathering more feedback

```html
<!DOCTYPE html>
<html lang="en">
<head>
<meta charset="utf-8">
<title>TEK Logistics – Core Values Banners</title>
<link rel="stylesheet" href="https://fonts.googleapis.com/css2?family=Montserrat:wght@700&family=Roboto:wght@500&family=Arimo:wght@400;700&display=swap">
<style>
  :root {
    --stage: #2b2926;
    --red: #d42a1e;
    --red-light: #e8483b;
    --ink: #2a2a2a;
    --paper: #ffffff;
    --photo-light: #c9c9c9;
    --photo-mid: #9a9a9a;
    --warehouse: #1e1d1c;
    --quote-mark: #d6d6d6;
  }
  html, body {
    margin: 0;
    width: 1200px;
    height: 1200px;
    overflow: hidden;
    background: var(--stage);
  }
  .banner {
    position: absolute;
    left: 58px;
    width: 1082px;
    height: 338px;
    display: block;
  }
  .banner--bars { top: 214px; }
  .banner--circles { top: 620px; }
  .brand-name {
    font-family: "Montserrat", sans-serif;
    font-weight: 700;
    font-size: 30px;
    fill: var(--ink);
  }
  .value-text {
    font-family: "Roboto", sans-serif;
    font-weight: 500;
    font-size: 21px;
    letter-spacing: 1.8px;
    fill: var(--paper);
  }
  .mission-text {
    font-family: "Arimo", sans-serif;
    font-size: 14.5px;
    fill: #1b1b1b;
  }
  .mission-text--large {
    font-family: "Arimo", sans-serif;
    font-size: 17.6px;
    fill: #1b1b1b;
  }
  .mission-strong { font-weight: 700; }
  .quote-mark {
    font-family: "Arimo", sans-serif;
    font-weight: 700;
    font-size: 120px;
    fill: var(--quote-mark);
  }
</style>
</head>
<body>

<!-- Banner one: stacked value bars -->
<svg class="banner banner--bars" viewBox="0 0 1082 338" xmlns="http://www.w3.org/2000/svg">
  <defs>
    <linearGradient id="crewPhoto" x1="0" y1="0" x2="1" y2="0">
      <stop offset="0" stop-color="#b8b8b8"/>
      <stop offset="0.5" stop-color="var(--photo-light)"/>
      <stop offset="1" stop-color="var(--photo-mid)"/>
    </linearGradient>
    <linearGradient id="redBar" x1="0" y1="0" x2="1" y2="0">
      <stop offset="0" stop-color="var(--red)"/>
      <stop offset="1" stop-color="var(--red-light)"/>
    </linearGradient>
  </defs>
  <rect class="panel-white" width="1082" height="338" fill="var(--paper)"/>
  <polygon role="img" aria-label="Greyscale photo of movers carrying a large white appliance outside a house" points="418,0 1082,0 1082,338 158,338" fill="url(#crewPhoto)"/>
  <polygon class="stripe-dark" points="357,0 418,0 158,338 154,338" fill="var(--ink)"/>
  <polygon class="stripe-red" points="400,0 418,0 162,338 152,338" fill="var(--red)"/>

  <g class="brand">
    <circle cx="54" cy="94" r="9" fill="var(--red)"/>
    <text class="brand-name" x="70" y="105">TEK Logistics</text>
  </g>

  <g class="values">
    <rect x="437" y="14" width="645" height="44" fill="url(#redBar)"/>
    <text class="value-text" x="760" y="43" text-anchor="middle">Do the right things for the right reasons</text>
    <rect x="512" y="66" width="570" height="46" fill="var(--ink)"/>
    <text class="value-text" x="777" y="96" text-anchor="middle">Pursue growth and development</text>
    <rect x="597" y="120" width="485" height="46" fill="url(#redBar)"/>
    <text class="value-text" x="850" y="150" text-anchor="middle">Build a positive team atmosphere</text>
    <rect x="678" y="174" width="404" height="45" fill="var(--ink)"/>
    <text class="value-text" x="887" y="203" text-anchor="middle">Deliver WOW through service</text>
    <rect x="762" y="227" width="320" height="46" fill="url(#redBar)"/>
    <text class="value-text" x="906" y="257" text-anchor="middle">Do everything Safely</text>
    <rect x="825" y="281" width="257" height="45" fill="var(--ink)"/>
    <text class="value-text" x="844" y="310">Have Fun</text>
  </g>

  <text class="mission-text" text-anchor="middle">
    <tspan x="522" y="250">”Provide the best customer experience</tspan>
    <tspan x="522" y="268">while creating an environment</tspan>
    <tspan x="522" y="287">of growth and opportunity for our</tspan>
    <tspan x="522" y="305">customers, employees, and service providers”</tspan>
  </text>
</svg>

<!-- Banner two: circle photos over warehouse -->
<svg class="banner banner--circles" viewBox="0 0 1082 338" xmlns="http://www.w3.org/2000/svg">
  <defs>
    <linearGradient id="warehousePhoto" x1="0" y1="0" x2="0" y2="1">
      <stop offset="0" stop-color="#2c2b2a"/>
      <stop offset="0.6" stop-color="var(--warehouse)"/>
      <stop offset="1" stop-color="#3a3631"/>
    </linearGradient>
    <linearGradient id="wrapPhoto" x1="0" y1="0" x2="1" y2="1">
      <stop offset="0" stop-color="#6b5a4a"/>
      <stop offset="1" stop-color="#e6e6e6"/>
    </linearGradient>
    <linearGradient id="moverPhoto" x1="0" y1="0" x2="1" y2="1">
      <stop offset="0" stop-color="#8fa0ad"/>
      <stop offset="1" stop-color="#4b4b4b"/>
    </linearGradient>
  </defs>
  <rect width="1082" height="338" fill="var(--paper)"/>
  <polygon role="img" aria-label="Dark photo of a warehouse floor stacked with boxed pallets" points="552,0 1082,0 1082,338 445,338" fill="url(#warehousePhoto)"/>
  <polygon class="stripe-red" points="542,0 552,0 445,338 418,338" fill="var(--red)"/>

  <g class="brand">
    <circle cx="30" cy="118" r="9" fill="var(--red)"/>
    <text class="brand-name" x="46" y="129">TEK Logistics</text>
  </g>

  <circle cx="332" cy="62" r="80" fill="var(--red)"/>
  <circle role="img" aria-label="Photo of a worker stretch-wrapping a pallet" cx="332" cy="62" r="73" fill="url(#wrapPhoto)"/>
  <circle cx="442" cy="194" r="52" fill="var(--ink)"/>
  <circle role="img" aria-label="Photo of a mover carrying a white appliance" cx="442" cy="194" r="48" fill="url(#moverPhoto)"/>

  <text class="quote-mark" x="10" y="270">“</text>
  <text class="quote-mark" x="262" y="400">”</text>
  <text class="mission-text--large">
    <tspan x="40" y="216">Provide the best customer experience</tspan>
    <tspan x="40" y="238">while creating an environment</tspan>
    <tspan x="40" y="259">of growth and opportunity for our</tspan>
    <tspan x="40" y="281"><tspan class="mission-strong">customers</tspan>, <tspan class="mission-strong">employees</tspan>,</tspan>
    <tspan x="40" y="302">and <tspan class="mission-strong">service providers</tspan></tspan>
  </text>

  <g class="values">
    <text class="value-text" x="574" y="76">Do the right things for the right reasons</text>
    <text class="value-text" x="566" y="117">Pursue growth and development</text>
    <text class="value-text" x="550" y="158">Build a positive team atmosphere</text>
    <text class="value-text" x="534" y="198">Deliver WOW through service</text>
    <text class="value-text" x="519" y="239">Do everything Safely</text>
    <text class="value-text" x="503" y="280">Have Fun</text>
  </g>
</svg>

</body>
</html>
```